Stationary for a Legal Support Company
Brimvale Courier & Records, Inc.
Stationary for a Legal Support Company - Marketing
Creative Brief
Professional
Rupert J Olwen
PO Box 712 4175 Marrow Ln Twinsburg OH 44087
tkorvel@brimcr.com
www.brimcr.com
Generic USB flash and CD/DVD layout also appreciated.
Back of the card can include the logo or logo/text.
tkorvel tkorvel
Thank you all for your submissions. I believe I have sent some comments to everyone who has entered a submission. If you did not receive a comment from me, please let me know.

```html
<!DOCTYPE html>
<html lang="en">
<head>
<meta charset="utf-8">
<title>Brimvale Courier &amp; Records, Inc. — Business Card</title>
<link rel="stylesheet" href="https://fonts.googleapis.com/css2?family=Open+Sans:wght@400;600;700&display=swap">
<style>
  :root {
    --backdrop: #2f3033;
    --card: #ffffff;
    --card-shade: #e4e5e8;
    --ink: #1d1d1f;
    --brand-blue: #2a58a6;
    --brand-navy: #1f3f7a;
    --muted: #3b3f46;
  }
  * { box-sizing: border-box; margin: 0; padding: 0; }
  html, body {
    width: 1200px; height: 816px; overflow: hidden;
    background: var(--backdrop);
    font-family: "Open Sans", Arial, sans-serif;
  }
  .card {
    position: absolute; left: 75px; top: 108px;
    width: 1050px; height: 600px;
    background: var(--card);
    border-radius: 36px;
    overflow: hidden;
  }
  .card-base {
    position: absolute; left: 0; bottom: 0; width: 1050px; height: 150px;
  }
  .holder { position: absolute; left: 84px; top: 200px; }
  .holder-name {
    font-size: 32px; font-weight: 700; letter-spacing: 0.5px;
    color: var(--ink); text-transform: uppercase; line-height: 1.1;
  }
  .holder-title {
    font-size: 24px; font-weight: 400; color: var(--brand-blue); margin-top: 4px;
  }
  .contact-list {
    position: absolute; left: 84px; top: 318px; list-style: none;
    font-size: 20px; color: var(--muted); font-weight: 600;
  }
  .contact-list li { display: flex; align-items: flex-start; gap: 12px; line-height: 28px; margin-bottom: 2px; }
  .contact-list svg { flex: none; width: 20px; height: 20px; margin-top: 4px; fill: var(--brand-navy); }
  .contact-list .address { width: 330px; }
  .brand { position: absolute; left: 590px; top: 170px; display: flex; align-items: center; gap: 20px; }
  .brand-dot { width: 92px; height: 92px; border-radius: 50%; border: 5px solid var(--brand-blue); }
  .brand-rule { width: 2px; height: 110px; background: var(--brand-navy); }
  .brand-name {
    font-size: 27px; font-weight: 400; color: var(--brand-navy);
    text-transform: uppercase; line-height: 1.15; letter-spacing: 1px;
  }
  .web-band {
    position: absolute; left: 560px; top: 296px; width: 520px; height: 58px;
    background: var(--brand-blue); border-radius: 29px;
    display: flex; align-items: center; padding-left: 44px;
    color: #fff; font-size: 27px; font-weight: 600; letter-spacing: 0.3px;
  }
</style>
</head>
<body>
  <main class="card">
    <svg class="card-base" viewBox="0 0 1050 150" aria-hidden="true">
      <path d="M0 70 H520 C560 70 570 40 610 40 H1050 V150 H0 Z" fill="var(--card-shade)"/>
      <path d="M610 40 H1050" stroke="var(--brand-blue)" stroke-width="0"/>
    </svg>

    <div class="holder">
      <h1 class="holder-name">Rupert J Olwen</h1>
      <p class="holder-title">Managing Director</p>
    </div>

    <ul class="contact-list">
      <li>
        <svg viewBox="0 0 24 24"><path d="M12 2a7 7 0 0 0-7 7c0 5 7 13 7 13s7-8 7-13a7 7 0 0 0-7-7zm0 9.5A2.5 2.5 0 1 1 12 6.5a2.5 2.5 0 0 1 0 5z"/></svg>
        <span class="address">PO Box 712 4175 Marrow Ln Twinsburg OH 44087</span>
      </li>
      <li>
        <svg viewBox="0 0 24 24"><path d="M6.6 10.8a15 15 0 0 0 6.6 6.6l2.2-2.2c.3-.3.7-.4 1-.2 1.1.4 2.3.6 3.6.6.6 0 1 .4 1 1V20c0 .6-.4 1-1 1A17 17 0 0 1 3 4c0-.6.4-1 1-1h3.5c.6 0 1 .4 1 1 0 1.3.2 2.5.6 3.6.1.3 0 .7-.2 1z"/></svg>
        <span>012 555 0147</span>
      </li>
      <li>
        <svg viewBox="0 0 24 24"><path d="M7 3h10v5H7zM4 9h16a1 1 0 0 1 1 1v8H3v-8a1 1 0 0 1 1-1zm3 6v5h10v-5z"/></svg>
        <span>012 555 0183</span>
      </li>
      <li>
        <svg viewBox="0 0 24 24"><path d="M3 5h18v14H3zm2 2v.4l7 5 7-5V7zm0 2.9V17h14V9.9l-7 5z"/></svg>
        <span>tkorvel@brimcr.com</span>
      </li>
    </ul>

    <div class="brand">
      <div class="brand-dot" aria-hidden="true"></div>
      <div class="brand-rule" aria-hidden="true"></div>
      <p class="brand-name">Brimvale<br>Courier &amp;<br>Records</p>
    </div>

    <div class="web-band">www.brimcr.com</div>
  </main>
</body>
</html>
```